Harbinger Roofing
Commercial - Industrial - Residential
Harbinger Roofing -
Creative Brief
Professional
Marcus Delvane
President
318 W. Tarkin Blvd. Anna, Tx 75412
marcus@harbingerroofing-example.com
www.HarbingerRoofing-example.com
24 Hr. Emergency Response and Repairs, Preventative Maintenance, Waterproofing, New Construction, Roof Replacement, PowerGlint Rated

```html
<!DOCTYPE html>
<html lang="en">
<head>
<meta charset="utf-8">
<title>Harbinger Roofing – Business Cards</title>
<link href="https://fonts.googleapis.com/css2?family=Tinos:wght@400;700&display=swap" rel="stylesheet">
<style>
  :root{
    --bg:#e9e6e2;
    --card:#ffffff;
    --navy:#1d3f6e;
    --ink:#3a3a3a;
    --blue:#1f86c0;
    --blue-deep:#145f96;
    --cyan:#6cc6ea;
    --rule:#c9ced6;
  }
  *{margin:0;padding:0;box-sizing:border-box}
  html,body{width:1200px;height:852px;overflow:hidden;background:var(--bg);font-family:"Tinos",serif;color:var(--ink)}
  .stage{position:relative;width:1200px;height:852px}
  .card{position:absolute;left:280px;width:640px;height:366px;background:var(--card);border-radius:26px;overflow:hidden;box-shadow:0 6px 18px rgba(0,0,0,.18)}
  .card--front{top:40px}
  .card--back{top:446px}
  .wordmark{color:var(--navy);font-weight:700;text-transform:uppercase;line-height:1;text-align:center}
  .wordmark .mark-dot{display:inline-block;width:10px;height:10px;border-radius:50%;background:var(--blue);vertical-align:middle;margin-left:6px}
  .tagline{color:var(--navy);font-size:11px;letter-spacing:1.5px;text-transform:uppercase;text-align:center;margin-top:8px;white-space:nowrap}
  .person-name{color:var(--navy);font-weight:700;font-size:19px}
  .person-title{color:var(--navy);font-size:15px;margin-top:2px}
  .address{font-size:14px;line-height:1.35;color:var(--ink)}
  .contacts{list-style:none;font-size:14px;color:var(--ink)}
  .contacts li{display:flex;align-items:center;gap:8px;line-height:20px}
  .contacts svg{width:12px;height:12px;fill:var(--navy);flex:none}
  .band{position:absolute;left:0;bottom:0;width:640px;height:96px}
  .website{position:absolute;left:0;right:0;bottom:16px;text-align:center;color:#fff;font-size:13px;line-height:16px}

  /* front layout */
  .card--front .brand{position:absolute;left:20px;top:118px;width:280px}
  .card--front .wordmark{font-size:26px}
  .card--front .tagline{font-size:10px;letter-spacing:0.8px}
  .card--front .divider{position:absolute;left:318px;top:36px;width:1px;height:210px;background:var(--rule)}
  .card--front .details{position:absolute;left:342px;top:38px}
  .card--front .address{margin-top:34px}
  .card--front .contacts{margin-top:34px}

  /* back layout */
  .card--back .brand{position:absolute;left:0;right:0;top:48px}
  .card--back .wordmark{font-size:36px}
  .card--back .details{position:absolute;left:60px;top:160px}
  .card--back .address{margin-top:24px}
  .card--back .divider{position:absolute;left:348px;top:160px;width:1px;height:110px;background:var(--rule)}
  .card--back .contacts{position:absolute;left:368px;top:160px}
</style>
</head>
<body>
<main class="stage">

  <section class="card card--front">
    <div class="brand">
      <div class="wordmark">Harbinger Roofing<span class="mark-dot"></span></div>
      <div class="tagline">Commercial • Industrial • Residential</div>
    </div>
    <div class="divider"></div>
    <div class="details">
      <div class="person-name">Marcus Delvane</div>
      <div class="person-title">President</div>
      <div class="address">318 W. Tarkin Blvd.<br>Anna, Tx 75412</div>
      <ul class="contacts">
        <li><svg viewBox="0 0 12 12"><path d="M3 1l2 2.5-1.2 1.3a7 7 0 003.4 3.4L8.5 7 11 9l-1.3 2C5.5 11 1 6.5 1 2.3z"/></svg>(T)877.555.0186</li>
        <li><svg viewBox="0 0 12 12"><path d="M3 1l2 2.5-1.2 1.3a7 7 0 003.4 3.4L8.5 7 11 9l-1.3 2C5.5 11 1 6.5 1 2.3z"/></svg>972.555.0135</li>
        <li><svg viewBox="0 0 12 12"><rect x="3" y="0" width="6" height="12" rx="1.2"/></svg>214.555.0130</li>
        <li><svg viewBox="0 0 12 12"><rect x="1" y="4" width="10" height="7" rx="1"/><rect x="3" y="0" width="6" height="4"/></svg>972.555.0140</li>
        <li><svg viewBox="0 0 12 12"><path d="M0 2h12v8H0z M0 2l6 4 6-4" /></svg>marcus@harbingerroofing-example.com</li>
      </ul>
    </div>
    <svg class="band" viewBox="0 0 640 96" preserveAspectRatio="none" aria-hidden="true">
      <defs>
        <linearGradient id="bandFront" x1="0" y1="0" x2="0" y2="1">
          <stop offset="0" stop-color="var(--blue)"/><stop offset="1" stop-color="var(--blue-deep)"/>
        </linearGradient>
      </defs>
      <path d="M0 18 C140 50 440 50 640 6 L640 96 L0 96 Z" fill="var(--cyan)"/>
      <path d="M0 28 C140 60 440 60 640 16 L640 96 L0 96 Z" fill="url(#bandFront)"/>
    </svg>
    <div class="website">www.HarbingerRoofing-example.com</div>
  </section>

  <section class="card card--back">
    <div class="brand">
      <div class="wordmark">Harbinger Roofing<span class="mark-dot"></span></div>
      <div class="tagline">Commercial • Industrial • Residential</div>
    </div>
    <div class="details">
      <div class="person-name">Marcus Delvane</div>
      <div class="person-title">President</div>
      <div class="address">318 W. Tarkin Blvd.<br>Anna, Tx 75412</div>
    </div>
    <div class="divider"></div>
    <ul class="contacts">
      <li><svg viewBox="0 0 12 12"><path d="M3 1l2 2.5-1.2 1.3a7 7 0 003.4 3.4L8.5 7 11 9l-1.3 2C5.5 11 1 6.5 1 2.3z"/></svg>(T)877.555.0186</li>
      <li><svg viewBox="0 0 12 12"><path d="M3 1l2 2.5-1.2 1.3a7 7 0 003.4 3.4L8.5 7 11 9l-1.3 2C5.5 11 1 6.5 1 2.3z"/></svg>972.555.0135</li>
      <li><svg viewBox="0 0 12 12"><rect x="3" y="0" width="6" height="12" rx="1.2"/></svg>214.555.0130</li>
      <li><svg viewBox="0 0 12 12"><rect x="1" y="4" width="10" height="7" rx="1"/><rect x="3" y="0" width="6" height="4"/></svg>972.555.0140</li>
      <li><svg viewBox="0 0 12 12"><path d="M0 2h12v8H0z M0 2l6 4 6-4" /></svg>marcus@harbingerroofing-example.com</li>
    </ul>
    <svg class="band" viewBox="0 0 640 96" preserveAspectRatio="none" aria-hidden="true">
      <defs>
        <linearGradient id="bandBack" x1="0" y1="0" x2="0" y2="1">
          <stop offset="0" stop-color="var(--blue)"/><stop offset="1" stop-color="var(--blue-deep)"/>
        </linearGradient>
      </defs>
      <path d="M0 26 C160 50 440 50 640 14 L640 96 L0 96 Z" fill="var(--cyan)"/>
      <path d="M0 36 C170 60 450 60 640 24 L640 96 L0 96 Z" fill="url(#bandBack)"/>
    </svg>
    <div class="website">www.HarbingerRoofing-example.com</div>
  </section>

</main>
</body>
</html>
```